Copper Brook Agency Website - Wordpress Web UPDATED BRIEF

FINAL LOGO UPLOADED - please look to this as reference for how we would like the site to look and feel.

We are a digital marketing agency - looking to have a new website built. We are looking for a simple one page feel of site that will allow us to grow it later. (Feel free to take some liberties with that if your imagination veers off) Must be very, playful, bold, sleek and easily integrate video. Wordpress only.

Overview:

Copper Brook is a creative constellation. We are built on what's great about the shared economy. With access to thousands of content creators, designers, technicians, writers, strategists and other creatives around the world, we are built differently than a traditional “brick and mortar” Marketing Agency. We provide the traditional services our clients have come to expect, without the “5X factor” of covering the overhead common in the old agency model. We believe even better work can be created in collaboration with our clients and by passing those savings back to them for their use. Our clients pay for our art, our work and our passion –not our furniture.

"Copper Brook, Let's Begin Today"

Target Market(s)

companies looking for creative agency help, video production, creative consulting and coaching

Industry/Entity Type

Digital Marketing

Coding

Coded - Design and coding required

Number of Pages Required

1 page

Font styles to use
Sans Serif

Colors
3277b5
33a6d7
ec1f27

Requirements
Must have
• Wordpress design is a must. Looking for a one sheet homepage - with sections that are all on the main front page. We will have videos to embed, and should be able to have client logos and easy access to show a variety of our creative work.
• Please look to the logo for how we would like the site to feel.
• Please think "icon process flow" instead of blocks of text (which we used to have). Use the text to explain what the process flow should represent - don't actually copy paste the text but show it visually in icons.
Nice to have
• innovation around how we show video content. solid colors complementary to our palette and aesthetic.
Should not have
• Standard HTML coding

```html
<!DOCTYPE html>
<html lang="en">
<head>
<meta charset="utf-8">
<title>Copper Brook Agency</title>
<link rel="stylesheet" href="https://fonts.googleapis.com/css2?family=Montserrat:wght@400;500;600;700;800&display=swap">
<style>
:root{
  --brand-red:#ec1f27;
  --brand-blue:#3277b5;
  --brand-sky:#33a6d7;
  --brand-navy:#1f4f7d;
  --ink:#222;
  --muted:#555;
  --paper:#ffffff;
  --card:#e9edf1;
  --night:#0b0d11;
}
*{box-sizing:border-box;margin:0;padding:0}
html,body{width:1200px;height:3664px;overflow:hidden;background:var(--paper)}
body{font-family:"Montserrat",sans-serif;color:var(--ink);position:relative}
section,header,footer,.topbar{position:absolute;left:0;width:1200px}

.btn{background:var(--brand-red);color:#fff;font:700 11px "Montserrat",sans-serif;display:flex;align-items:center;justify-content:center;letter-spacing:.5px}

/* top bar */
.topbar{top:0;height:32px;background:var(--brand-blue);color:#fff;font:500 10px "Montserrat",sans-serif;display:flex;align-items:center;padding:0 164px;justify-content:space-between}
.topbar .contact span{margin-right:22px}
.topbar .social{display:flex;gap:12px}
.topbar .social i{width:12px;height:12px;border-radius:50%;background:#fff;display:block}

/* nav */
.site-nav{top:32px;height:80px;display:flex;align-items:center;justify-content:space-between;padding:0 164px 0 232px;background:#fff}
.brand{display:flex;align-items:center;gap:8px;font:800 26px "Montserrat",sans-serif;color:var(--brand-red);letter-spacing:.5px}
.brand i{width:14px;height:14px;background:var(--brand-red);border-radius:50%;display:block}
.menu{display:flex;gap:26px;font:700 11px "Montserrat",sans-serif;color:var(--brand-blue)}

/* hero */
.hero{top:112px;height:676px}
.hero .photo{position:absolute;inset:0;background:linear-gradient(135deg,#a0714a 0%,#c39467 45%,#8e5f3a 100%)}
.hero .shade{position:absolute;inset:0;background:rgba(0,0,0,.14)}
.hero h1{position:absolute;top:228px;left:0;width:1200px;text-align:center;font:500 36px/56px "Montserrat",sans-serif;color:#fff;letter-spacing:1px;text-shadow:0 2px 6px rgba(0,0,0,.35)}
.hero .btn{position:absolute;left:448px;top:390px;width:224px;height:46px}

/* about */
.about{top:788px;height:732px}
.about h2{position:absolute;left:160px;top:28px;font:600 50px "Montserrat",sans-serif;color:var(--brand-red);letter-spacing:2px}
.about h3{position:absolute;left:160px;top:104px;font:700 24px/52px "Montserrat",sans-serif;color:var(--brand-blue);letter-spacing:.5px}
.about h3 em{font-style:normal;color:var(--brand-red)}
.about p{position:absolute;left:160px;width:420px;font:400 10px/19px "Montserrat",sans-serif;color:var(--muted);text-transform:uppercase}
.about .p1{top:244px}
.about .p2{top:344px}
.about .btn{position:absolute;left:160px;top:468px;width:200px;height:50px}
.about .shot{position:absolute;left:608px;width:424px}
.about .s1{top:0;height:244px;background:linear-gradient(160deg,#8b8d91,#cfd1d4 55%,#6d7074)}
.about .s2{top:244px;height:240px;background:linear-gradient(160deg,#dadcdf,#f2f2f2 55%,#b4b7bb)}
.about .s3{top:484px;height:248px;background:linear-gradient(160deg,#c9c2b4,#ece6db 50%,#5b5f66)}

/* services as a process flow */
.services{top:1520px;height:392px}
.services h2{position:absolute;top:52px;width:1200px;text-align:center;font:600 42px "Montserrat",sans-serif;color:var(--brand-red);letter-spacing:2px}
.flow-arrows{position:absolute;left:0;top:136px}
.service{position:absolute;top:136px;width:220px;text-align:center}
.service svg{display:block;margin:0 auto}
.service h4{margin-top:20px;font:700 11px "Montserrat",sans-serif;color:var(--ink)}
.service p{margin-top:8px;font:400 8px "Montserrat",sans-serif;color:var(--muted);text-transform:uppercase}
.service .rule{width:90px;height:3px;background:var(--brand-red);margin:14px auto 0}

/* video */
.video{top:1912px;height:576px}
.video .photo{position:absolute;inset:0;background:linear-gradient(120deg,#1b1f26,#4a5260 50%,#20242b)}
.video .shade{position:absolute;inset:0;background:rgba(10,20,35,.45)}
.video .play{position:absolute;left:528px;top:120px}
.video h2{position:absolute;top:214px;width:1200px;text-align:center;font:700 44px "Montserrat",sans-serif;color:#fff}
.video p{position:absolute;top:296px;left:260px;width:680px;text-align:center;font:600 15px/30px "Montserrat",sans-serif;color:#fff}

/* news */
.news{top:2488px;height:424px}
.news h2{position:absolute;left:164px;top:44px;font:600 42px "Montserrat",sans-serif;color:var(--brand-red);letter-spacing:1px}
.news h2 span{color:var(--brand-blue)}
.card{position:absolute;top:140px;width:280px;height:270px;background:var(--card)}
.card .thumb{height:168px}
.card p{margin:12px 14px 0;font:500 8px/14px "Montserrat",sans-serif;color:var(--muted);text-transform:uppercase}
.card .btn{margin:12px 14px 0;width:70px;height:20px;font-size:7px;background:var(--brand-blue)}

/* testimonials */
.testimonials{top:2912px;height:376px;background:#141416}
.testimonials .photo{position:absolute;inset:0;background:linear-gradient(110deg,#0e0f12,#2c3038 55%,#111215)}
.testimonials h2{position:absolute;top:30px;width:1200px;text-align:center;font:500 40px "Montserrat",sans-serif;color:#fff;letter-spacing:2px}
.testimonials .avatar{position:absolute;left:560px;top:124px;width:80px;height:80px;border-radius:50%;background:linear-gradient(#8a7a70,#4a3c36);border:3px solid #fff}
.testimonials q{position:absolute;top:236px;width:1200px;text-align:center;font:500 11px "Montserrat",sans-serif;color:#ddd;text-transform:uppercase;quotes:"\201C" "\201D"}
.clients{position:absolute;top:292px;left:330px;width:540px;display:flex;justify-content:space-between}
.clients i{display:block;width:80px;height:34px;border-radius:6px;background:rgba(255,255,255,.16)}

/* footer */
.site-footer{top:3288px;height:376px;background:var(--night);color:#fff}
.form{position:absolute;left:164px;top:40px;width:276px}
.field{background:#fff;color:#777;font:400 11px "Montserrat",sans-serif;height:40px;padding:13px 12px;margin-bottom:24px}
.field.msg{height:64px}
.form .btn{width:276px;height:38px;font:700 12px "Montserrat",sans-serif;justify-content:flex-start;padding-left:12px}
.links{position:absolute;left:540px;top:40px}
.links h5,.address h5{font:700 15px "Montserrat",sans-serif;margin-bottom:20px}
.links li{list-style:none;font:400 11px "Montserrat",sans-serif;color:var(--brand-sky);margin-bottom:22px}
.address{position:absolute;left:768px;top:40px;width:300px}
.address li{list-style:none;font:600 10px/16px "Montserrat",sans-serif;margin-bottom:20px;display:flex;gap:8px}
.address li i{width:10px;height:10px;background:var(--brand-red);display:block;margin-top:3px;flex:none}
</style>
</head>
<body>

<div class="topbar">
  <div class="contact"><span>+01 555 0148 · +01 555 0149</span><span>hello@copperbrook.com · 9 AM – 6 PM</span></div>
  <div class="social"><i></i><i></i><i></i></div>
</div>

<header class="site-nav">
  <div class="brand"><i></i>Copper Brook</div>
  <nav class="menu"><span>HOME</span><span>ABOUT</span><span>SERVICES</span><span>TESTIMONIALS</span><span>CONTACT US</span></nav>
</header>

<section class="hero">
  <div class="photo" role="img" aria-label="Top view of a wooden desk with a laptop, potted plant, sticky notes, coffee and a mouse"></div>
  <div class="shade"></div>
  <h1>WELCOME TO CREATIVE WORLD<br>AWESOME TECHNOLOGY</h1>
  <div class="btn">READ MORE</div>
</section>

<section class="about">
  <h2>ABOUT US</h2>
  <h3>LOOKING AN <em>ADEQUATE</em><br>SOLUTION FOR <em>YOUR</em></h3>
  <p class="p1">We shape bold stories for growing brands, pairing sharp strategy with playful design so every campaign feels fresh, clear and ready to reach the right people at the right moment.</p>
  <p class="p2">Our network of writers, designers and filmmakers works side by side with you, turning big ideas into sleek video, content and social work that keeps your audience coming back.</p>
  <div class="btn">READ MORE</div>
  <div class="shot s1" role="img" aria-label="Laptop and phone on a desk"></div>
  <div class="shot s2" role="img" aria-label="Hands typing on a laptop beside a phone"></div>
  <div class="shot s3" role="img" aria-label="Laptop with a coffee cup and plant on a desk"></div>
</section>

<section class="services">
  <h2>SERVICES</h2>
  <svg class="flow-arrows" width="1200" height="100" viewBox="0 0 1200 100">
    <g stroke="var(--brand-sky)" stroke-width="3" fill="var(--brand-sky)">
      <line x1="332" y1="50" x2="408" y2="50"/><path d="M416 50 L404 43 L404 57 Z"/>
      <line x1="544" y1="50" x2="636" y2="50"/><path d="M644 50 L632 43 L632 57 Z"/>
      <line x1="772" y1="50" x2="856" y2="50"/><path d="M864 50 L852 43 L852 57 Z"/>
    </g>
  </svg>
  <div class="service" style="left:158px">
    <svg width="100" height="100" viewBox="0 0 100 100"><circle cx="50" cy="50" r="48" fill="var(--brand-sky)"/><rect x="28" y="32" width="44" height="28" rx="2" fill="#fff"/><rect x="44" y="60" width="12" height="8" fill="#fff"/><rect x="36" y="68" width="28" height="3" fill="#fff"/></svg>
    <h4>Website Development</h4><p>Fast, clean sites built to grow</p><div class="rule"></div>
  </div>
  <div class="service" style="left:370px">
    <svg width="100" height="100" viewBox="0 0 100 100"><circle cx="50" cy="50" r="48" fill="var(--brand-sky)"/><circle cx="46" cy="46" r="14" fill="none" stroke="#fff" stroke-width="5"/><line x1="56" y1="56" x2="70" y2="70" stroke="#fff" stroke-width="6" stroke-linecap="round"/></svg>
    <h4>Search Engine Optimization</h4><p>Get found by the right people</p><div class="rule"></div>
  </div>
  <div class="service" style="left:598px">
    <svg width="100" height="100" viewBox="0 0 100 100"><circle cx="50" cy="50" r="45" fill="#fff" stroke="var(--brand-blue)" stroke-width="6"/><line x1="34" y1="68" x2="66" y2="32" stroke="var(--brand-blue)" stroke-width="8" stroke-linecap="round"/></svg>
    <h4>Content Writing</h4><p>Words that move your readers</p><div class="rule"></div>
  </div>
  <div class="service" style="left:818px">
    <svg width="100" height="100" viewBox="0 0 100 100"><circle cx="50" cy="50" r="46" fill="#eaf4fa" stroke="#b9d3e6" stroke-width="2"/><g stroke="#8fb3cf" stroke-width="2"><line x1="30" y1="34" x2="43" y2="45"/><line x1="70" y1="34" x2="57" y2="45"/><line x1="30" y1="66" x2="43" y2="55"/><line x1="70" y1="66" x2="57" y2="55"/></g><circle cx="50" cy="50" r="10" fill="var(--brand-sky)"/><circle cx="26" cy="30" r="6" fill="var(--brand-red)"/><circle cx="74" cy="30" r="6" fill="var(--brand-blue)"/><circle cx="26" cy="70" r="6" fill="var(--brand-blue)"/><circle cx="74" cy="70" r="6" fill="var(--brand-red)"/></svg>
    <h4>Social Media Marketing</h4><p>Campaigns people love to share</p><div class="rule"></div>
  </div>
</section>

<section class="video">
  <div class="photo" role="img" aria-label="Business team standing and talking in an office"></div>
  <div class="shade"></div>
  <svg class="play" width="72" height="72" viewBox="0 0 72 72"><circle cx="36" cy="36" r="36" fill="#fff"/><circle cx="36" cy="36" r="14" fill="var(--brand-red)"/></svg>
  <h2>Live Video Play</h2>
  <p>See how our creators plan, shoot and edit short films for brands of every size. Press play to watch a real project move from first idea to final cut, and discover how video can give your story a louder, bolder voice online.</p>
</section>

<section class="news">
  <h2>LATEST <span>NEWS</span></h2>
  <article class="card" style="left:164px"><div class="thumb" role="img" aria-label="Laptop and plant on a white desk" style="background:linear-gradient(150deg,#cfd2d6,#f3f3f3 55%,#8f949a)"></div><p>New ways to tell your brand story with short video</p><div class="btn">READ MORE</div></article>
  <article class="card" style="left:464px"><div class="thumb" role="img" aria-label="Laptop on a wooden table" style="background:linear-gradient(150deg,#8e6a4a,#c9a27c 55%,#5c5f66)"></div><p>How a clear process keeps every project on track</p><div class="btn">READ MORE</div></article>
  <article class="card" style="left:760px"><div class="thumb" role="img" aria-label="Hands using a phone above a laptop" style="background:linear-gradient(150deg,#d8dadc,#f5f5f5 55%,#9da2a8)"></div><p>Simple social tips that help small teams stand out</p><div class="btn">READ MORE</div></article>
</section>

<section class="testimonials">
  <div class="photo" role="img" aria-label="Dark blurred office background"></div>
  <h2>TESTIMONIALS</h2>
  <div class="avatar" role="img" aria-label="Client portrait"></div>
  <q>They turned our rough ideas into a bold video campaign our clients still talk about</q>
  <div class="clients" aria-label="Client brands"><i></i><i></i><i></i><i></i><i></i></div>
</section>

<footer class="site-footer">
  <div class="form">
    <div class="field">Name</div>
    <div class="field">Email</div>
    <div class="field msg">Message</div>
    <div class="btn">Submit</div>
  </div>
  <div class="links">
    <h5>Useful Links</h5>
    <ul><li>Home</li><li>About Us</li><li>Services</li><li>Testimonials</li><li>Contact Us</li></ul>
  </div>
  <div class="address">
    <h5>Address Information</h5>
    <ul>
      <li><i></i>Location : 48 Millrace Road, Ashford Vale</li>
      <li><i></i>Email : hello@copperbrook.com</li>
      <li><i></i>Phone : +01 555 0148</li>
    </ul>
  </div>
</footer>

</body>
</html>
```